Product Catalogue for Brand New Range in Growing Small Business

We require a product catalogue for a new range (bollards and barriers) to be supplied to industrial and commercial customers within New Zealand. There will be about three variations to display of one product, one-two images of each product. We already supply FRP, steel, and safety products nationwide. We have the required files and text copy, including branding guidelines to follow. Clean, professional style designed to clearly communicate and showcase new products to customers. I have supplied images showing examples of what the products look like, some inspiration and what current branding looks like. Black, white, grey.

Target Market(s)

Industrial, Commercial, Warehouse

Industry/Entity Type

Industrial, Commercial, Warehouse Environments

Font styles to use
Other font styles liked:
• Poppins

Colors

Designer to choose colors to be used in the design.

Requirements
Must have
• Our supplied copy and images, company branding applied

```html
<!DOCTYPE html>
<html lang="en">
<head>
<meta charset="utf-8">
<title>Bollards and Barriers Catalogue Pages</title>
<link rel="stylesheet" href="https://fonts.googleapis.com/css2?family=Archivo:wght@700;800&family=Poppins:ital,wght@0,400;0,500;0,600;0,700;1,400&family=Roboto:ital,wght@1,400&display=swap">
<style>
  :root {
    --stage: #4a4a4a;
    --page-grey: #c9c9c9;
    --black: #0a0a0a;
    --white: #ffffff;
    --ink: #1a1a1a;
    --panel-dark: rgba(28, 28, 28, 0.92);
    --rule: #222222;
  }
  * { box-sizing: border-box; margin: 0; padding: 0; }
  html, body { width: 1200px; height: 600px; overflow: hidden; }
  body { background: var(--stage); position: relative; font-family: "Poppins", sans-serif; color: var(--ink); }

  .page { position: absolute; top: 64px; width: 332px; height: 464px; background: var(--page-grey); overflow: hidden; }
  .page--case { left: 68px; }
  .page--bollards { left: 434px; }
  .page--barriers { left: 800px; }

  .page-shapes { position: absolute; inset: 0; width: 332px; height: 464px; }

  .title-tab { position: absolute; left: 31.5px; top: 29px; width: 163px; height: 41px; z-index: 2; }
  .title-tab svg { position: absolute; inset: 0; }
  .title-tab h1 { position: relative; font-family: "Archivo", sans-serif; font-weight: 800; font-size: 16.5px; color: var(--white); letter-spacing: 0.2px; line-height: 41px; padding-left: 14px; }

  /* Case study page */
  .case-kicker { position: absolute; left: 33.5px; top: 81px; font-family: "Roboto", sans-serif; font-style: italic; font-size: 12px; color: #333; }
  .case-title { position: absolute; left: 34px; top: 95px; font-weight: 700; font-size: 11.5px; line-height: 12.5px; color: #222; }
  .case-photo { position: absolute; inset: 0; }
  .case-story { position: absolute; left: 31.5px; top: 139.5px; width: 269px; height: 147px; background: var(--panel-dark); color: var(--white); padding: 13px 22px 0 12.5px; }
  .case-story p { font-size: 8.1px; line-height: 14px; font-weight: 400; }
  .case-meta { position: absolute; left: 12.5px; top: 117px; display: flex; gap: 10px; font-size: 5.4px; }
  .case-meta dt { font-weight: 600; margin-bottom: 4px; }
  .case-meta dd { font-weight: 400; }
  .case-meta .meta-item:nth-child(1) { width: 85px; }
  .case-meta .meta-item:nth-child(2) { width: 30px; }
  .solution { position: absolute; left: 31.5px; top: 313px; width: 268.5px; height: 124px; background: var(--white); padding: 9px 16px 0 9px; }
  .solution h2 { font-size: 8.3px; font-weight: 600; margin-bottom: 1.5px; }
  .solution ul { list-style: none; font-family: Arial, "Helvetica", sans-serif; font-size: 7.6px; line-height: 8.8px; color: #222; }
  .solution li { position: relative; padding-left: 9px; }
  .solution li::before { content: ""; position: absolute; left: 1.5px; top: 2.8px; width: 3.5px; height: 3.5px; border-radius: 50%; background: #bbb; }

  /* Product pages */
  .product-lede { position: absolute; left: 34px; top: 80px; font-size: 10.2px; line-height: 12.3px; font-weight: 400; color: #111; z-index: 2; }
  .thumb { position: absolute; left: 31.5px; top: 157.5px; width: 53.5px; height: 114px; background: var(--white); }
  .thumb-fill { position: absolute; left: 14px; top: 10px; width: 26px; height: 96px; background: linear-gradient(180deg, #fff7d6, #f6d66a); }
  .thumb-fill--dark { background: linear-gradient(180deg, #e6e6e6, #5a5a5a); }
  .thumb-caption { position: absolute; left: 31.5px; top: 278px; width: 52px; height: 18.5px; background: var(--black); }
  .drawing { position: absolute; background: linear-gradient(180deg, #fffdf3, #fbefc2); }
  .page--bollards .drawing { left: 118px; top: 122px; width: 188px; height: 154px; }
  .page--barriers .drawing { left: 115px; top: 156px; width: 192px; height: 125px; background: linear-gradient(90deg, #f1f1f1, #fbefc2 50%, #f1f1f1); }

  .spec-table { position: absolute; left: 31.5px; top: 303.5px; width: 268px; border-collapse: collapse; background: var(--white); font-size: 6.2px; }
  .spec-table th, .spec-table td { border: 0.75px solid var(--rule); }
  .spec-table th { height: 17px; font-size: 7px; font-weight: 600; }
  .spec-table .part { width: 69px; text-align: center; font-size: 6.6px; line-height: 7px; }
  .spec-table .desc { padding: 3px 2px 0 5px; line-height: 8px; vertical-align: top; }
  .spec-table .row-pipe { height: 40px; }
  .spec-table .row-base { height: 34px; }
  .spec-table .row-ground { height: 40px; }
  .spec-table .row-ground .desc { padding-top: 9px; }
  .spec-table .row-base .part { padding-top: 8px; }
</style>
</head>
<body>

<section class="page page--case">
  <svg class="page-shapes" viewBox="0 0 332 464" aria-hidden="true">
    <polygon points="231,299 332,299 332,464 77,464" fill="var(--black)"/>
  </svg>
  <svg class="case-photo" viewBox="0 0 332 464" role="img" aria-label="Photo of yellow bollards lining a walkway beside a brown fence">
    <defs>
      <linearGradient id="photoTone" x1="0" y1="0" x2="1" y2="0">
        <stop offset="0" stop-color="#8a6a58"/>
        <stop offset="0.55" stop-color="#9c7d4a"/>
        <stop offset="1" stop-color="#e6b400"/>
      </linearGradient>
    </defs>
    <polygon points="256,0 332,0 332,212 245,299 100,299 100,156" fill="url(#photoTone)"/>
  </svg>
  <div class="title-tab">
    <svg viewBox="0 0 163 41" width="163" height="41" aria-hidden="true"><polygon points="0,0 163,0 122,41 0,41" fill="var(--black)"/></svg>
    <h1>BOLLARDS</h1>
  </div>
  <p class="case-kicker">Case Study:</p>
  <p class="case-title">Protecting road<br>with Bollard</p>
  <div class="case-story">
    <p>Urban foot traffic was threatening the health of exposed tree roots in a high-use walkway. We supplied FRP micro mesh grating to provide a protective, non-slip surface that maintains pedestrian comfort while preserving the natural landscape. The installation provided long-term protection and access without disturbing the surrounding environment.</p>
    <dl class="case-meta">
      <div class="meta-item"><dt>Location:</dt><dd>Urban walkway, New Zealand</dd></div>
      <div class="meta-item"><dt>Product:</dt><dd>Bollard</dd></div>
      <div class="meta-item"><dt>Industry:</dt><dd>Public Infrastructure</dd></div>
    </dl>
  </div>
  <div class="solution">
    <h2>Our Solution</h2>
    <ul>
      <li>We supplied FRP micro mesh grating to act as an effective barrier between the tree roots and the pedestrian path.</li>
      <li>The grating's lightweight, strong, and flexible structure made it ideal for covering uneven surfaces and adapting to natural contours around the tree.</li>
      <li>With a 7 mm aperture and fine grit surface, the grating provided a non-slip, comfortable walking surface suitable for both bare feet and all types of footwear.</li>
      <li>The design helped keep the soil loose, prevent erosion, and could be custom-shaped to fit the specific size and layout of each tree.</li>
    </ul>
  </div>
</section>

<section class="page page--bollards">
  <svg class="page-shapes" viewBox="0 0 332 464" aria-hidden="true">
    <polygon points="253,0 332,0 332,208 243,297 100.5,297 100.5,152" fill="var(--white)"/>
    <polygon points="235,297 332,297 332,464 75,464" fill="var(--black)"/>
  </svg>
  <div class="title-tab">
    <svg viewBox="0 0 163 41" width="163" height="41" aria-hidden="true"><polygon points="0,0 163,0 122,41 0,41" fill="var(--black)"/></svg>
    <h1>BOLLARDS</h1>
  </div>
  <p class="product-lede">Protect independent<br>areas such as<br>isolation, gate, etc</p>
  <div class="thumb"><div class="thumb-fill" role="img" aria-label="Render of a yellow bollard with base plate"></div></div>
  <div class="thumb-caption"></div>
  <div class="drawing" role="img" aria-label="Dimension drawing of three yellow bollards, diameter 125, heights 500, 750 and 1000"></div>
  <table class="spec-table">
    <tr><th class="part">Parts</th><th>Descrition</th></tr>
    <tr class="row-pipe"><td class="part">Pipe</td><td class="desc">Developed by imported polymer plastic, which have strong weather and chemical not easy to age; natural imported color with low chemical activity, UV resistance meets ISO ISO4892-3 corrosion.</td></tr>
    <tr class="row-base"><td class="part">Base</td><td class="desc">Metal, rubber and other materials combined assembly, exposed metal is tread by coating withstand 500 hours exposure to neutral salt spray with no rust.</td></tr>
    <tr class="row-ground"><td class="part">Ground<br>Connection</td><td class="desc">Fixed bay inverted cone chemical anchor bolt, with dacromet, withstand 1000 hours exposure<br>neutral salt spray with no rust; fastened by Ss304 cap nut.</td></tr>
  </table>
</section>

<section class="page page--barriers">
  <svg class="page-shapes" viewBox="0 0 332 464" aria-hidden="true">
    <polygon points="254.5,0 332,0 332,208 243,297 100.5,297 100.5,152" fill="var(--white)"/>
    <polygon points="235,297 332,297 332,464 75,464" fill="var(--black)"/>
  </svg>
  <div class="title-tab">
    <svg viewBox="0 0 163 41" width="163" height="41" aria-hidden="true"><polygon points="0,0 163,0 122,41 0,41" fill="var(--black)"/></svg>
    <h1>LD BARRIERS</h1>
  </div>
  <p class="product-lede">Protect independent<br>areas such as<br>isolation, road, etc</p>
  <div class="thumb"><div class="thumb-fill thumb-fill--dark" role="img" aria-label="Dimension drawing of a black barrier post, height 1160, diameter 125"></div></div>
  <div class="thumb-caption"></div>
  <div class="drawing" role="img" aria-label="Dimension drawing of a barrier with two black posts and three yellow rails, span 600 to 1800"></div>
  <table class="spec-table">
    <tr><th class="part">Parts</th><th>Descrition</th></tr>
    <tr class="row-pipe"><td class="part">Pipe</td><td class="desc">Developed by imported polymer plastic, which have strong weather and chemical to age; natural imported color with low chemical activity, UV resistance meets ISO ISO48 corrosion.</td></tr>
    <tr class="row-base"><td class="part">Base</td><td class="desc">Metal, rubber and other materials care assembled in combination, and the metal is treated with elecrophoresis. The neutral saltspray test will not rust for 72 hours.</td></tr>
    <tr class="row-ground"><td class="part">Ground<br>Connection</td><td class="desc">Fixed by inverted cone chemical anchor bolt, with<br>dacromet, withstand 1000 hours exposure<br>neutral salt spray with no rust;</td></tr>
  </table>
</section>

</body>
</html>
```